Double-sided business card needed - specific brief

We need a double sided business card designed for our company Radiant Trimline. Having lost a lot of weight myself, the back of the card needs to show my before and after pictures. It needs to cover the entire back side of the card. This might be with my two before pictures over set on top of my main after picture or in separate frames. I'll leave that to your artistic consideration. The front needs to have our logo with contact details centred below.

The cards will be printed by PRINTKO.com and will be rectangular, 84mm x 55mm, but with ROUNDED edges. Please therefore present your designs rectangular but with rounded edges if possible.

The card should be designed in LANDSCAPE orientation.

As well as the logo, the front of the card should have the following details:

Moira Blakewell
Weight Loss Motivator with 189lb personal loss
moira@radiant-trimline.example
+44 (0)7700 900418

The website is important so should perhaps be more bold than the rest:
www.radiant-trimline.example

My brand colours are: Pink #CD2366, Light Pink #FD88AD. Blue #1C9CB1, Light Blue #64C4DE

Target Market(s)

Women 30+

Contact Information for Business Card

As description above

Font styles to use
Sans Serif

Requirements
Must have
• Double sided.
• Back side entirely covered with my before and after pictures.
• You may wish to float my before pictures on top of my after picture or add them in different frames. I look forward to seeing your different suggestions.

```html
<!DOCTYPE html>
<html lang="en">
<head>
<meta charset="utf-8">
<title>Radiant Trimline – Business Card Front</title>
<link href="https://fonts.googleapis.com/css2?family=Quicksand:wght@500&display=swap" rel="stylesheet">
<style>
  :root {
    --pink: #e3168c;
    --aqua: #40e6c9;
    --paper: #ffffff;
    --shade: rgba(0, 0, 0, 0.28);
  }
  html, body {
    margin: 0;
    padding: 0;
    overflow: hidden;
    background: var(--paper);
  }
  .card {
    position: relative;
    width: 1200px;
    height: 805px;
    background: var(--paper);
    overflow: hidden;
    font-family: "Quicksand", sans-serif;
    font-weight: 500;
  }
  .card__arc {
    position: absolute;
    inset: 0;
    width: 1200px;
    height: 805px;
  }
  .card__arc path {
    fill: var(--paper);
    filter: drop-shadow(0 10px 12px var(--shade));
  }
  .brand {
    position: absolute;
    left: 0;
    top: 90px;
    width: 1200px;
    text-align: center;
    color: var(--pink);
  }
  .brand__dot {
    display: block;
    width: 176px;
    height: 176px;
    margin: 0 auto;
    border-radius: 50%;
    background: var(--pink);
  }
  .brand__name {
    margin: 52px 0 0;
    font-size: 78px;
    line-height: 1;
    letter-spacing: 3px;
    text-transform: uppercase;
    font-weight: 500;
  }
  .brand__sub {
    margin: 16px 0 0;
    font-size: 36px;
    line-height: 1;
    letter-spacing: 2px;
    text-transform: uppercase;
  }
  .contact {
    position: absolute;
    left: 0;
    top: 522px;
    width: 1200px;
    text-align: center;
  }
  .contact__name {
    margin: 0;
    color: var(--pink);
    font-size: 41px;
    line-height: 50px;
  }
  .contact__role,
  .contact__lines {
    margin: 0;
    color: var(--aqua);
    font-size: 34px;
    line-height: 50px;
  }
  .contact__lines span + span { margin-left: 16px; }
  .contact__web {
    margin: 8px 0 0;
    color: var(--pink);
    font-size: 42px;
    line-height: 50px;
  }
</style>
</head>
<body>
  <main class="card">
    <svg class="card__arc" viewBox="0 0 1200 805" aria-hidden="true">
      <path d="M-20,-20 L-20,205 C150,410 400,478 610,474 C830,470 1080,392 1220,160 L1220,-20 Z"/>
    </svg>

    <header class="brand">
      <span class="brand__dot" aria-hidden="true"></span>
      <h1 class="brand__name">Radiant</h1>
      <p class="brand__sub">Trimline</p>
    </header>

    <section class="contact">
      <p class="contact__name">Moira Blakewell</p>
      <p class="contact__role">Weight Loss Motivator with 189lb personal loss</p>
      <p class="contact__lines"><span>moira@radiant-trimline.example</span><span>+44 (0)7700 900418</span></p>
      <p class="contact__web">www.radiant-trimline.example</p>
    </section>
  </main>
</body>
</html>
```